Business Cards for new orthopaedic surgery practice

My husband and I are starting our own orthopaedic surgery practice. We are looking for a business card that is uniform, but one will have my name/title and the other will have his. You can just create one design with my name on it for now. But when I choose your design as the winning design I will ask that you add another copy with his name/title.

We are looking for classy, simple, elite all in one. We like dark blues/a little gold/yellow. Something that goes with our logo. We want our logo incorporated. Here is all the info you need:
Business name: RV Spine & Vitality Center
Location: 38915 North Bramble Ave
Willow Harbor, FL 34987
Phone: 954-218-4630
Fax: 954-571-2846
Email: info@myrvspine.example

Names: Lucinda Ferrow, M.D.
Board Certified Hand and Upper Extremity Surgeon

Emeka Dlunga, M.D.
Board Certified Hip & Knee Replacement/General Orthopaedic Surgeon

Can decide what you want to put on the back. Maybe a slogan:
Rooted in Care. Focused on You

I am just going to upload our logo. The only thing is if we select you as the winning design, the location, and phone numbers may change. We will need your help to update that once fully solidified.

Industry/Entity Type

Medical

Contact Information for Business Card

Colors
0054AA
0677BA
7BADD7
CADEEF
E8F1F8
0094D4
00A9DD
6FCCEA
C7EBF8
E9F6FB

Requirements
Must have
• class, appeal,
Should not have
• We want to air on the side of masculine if we are looking at masculine vs. feminine feel. But we still want it classy, sophisticated, and something we will love

```html
<!DOCTYPE html>
<html lang="en">
<head>
<meta charset="utf-8">
<title>RV Spine &amp; Vitality Center – Business Card</title>
<link rel="stylesheet" href="https://fonts.googleapis.com/css2?family=Montserrat:wght@500;600&display=swap">
<style>
  :root {
    --backdrop: #3a3b3e;
    --navy: #1f2d5c;
    --navy-deep: #1a2650;
    --navy-soft: #2f3f75;
    --gold: #c9a55a;
    --white: #ffffff;
  }
  html, body {
    margin: 0;
    width: 1200px;
    height: 1200px;
    overflow: hidden;
    background: var(--backdrop);
    font-family: "Montserrat", sans-serif;
  }
  .canvas {
    position: relative;
    width: 1200px;
    height: 1200px;
  }
  .card {
    position: absolute;
    left: 180px;
    width: 840px;
    height: 480px;
    border-radius: 36px;
    overflow: hidden;
    box-shadow: 0 0 0 3px var(--gold), 0 18px 40px rgba(0,0,0,0.35);
  }
  .card--front { top: 90px; }
  .card--back {
    top: 630px;
    background: linear-gradient(160deg, var(--navy-soft) 0%, var(--navy) 45%, var(--navy-deep) 100%);
    display: flex;
    align-items: center;
    justify-content: center;
  }
  .card__shapes {
    position: absolute;
    inset: 0;
  }
  .brand {
    display: flex;
    align-items: center;
    gap: 16px;
    white-space: nowrap;
  }
  .brand__dot {
    width: 22px;
    height: 22px;
    border-radius: 50%;
    flex: none;
  }
  .brand__name {
    font-weight: 600;
    letter-spacing: 0.06em;
    text-transform: uppercase;
    line-height: 1.25;
  }
  .card--front .brand {
    position: absolute;
    left: 470px;
    top: 150px;
    color: var(--navy);
  }
  .card--front .brand__dot { background: var(--navy); }
  .card--front .brand__name { font-size: 26px; }
  .card--back .brand {
    position: relative;
    color: var(--navy-soft);
  }
  .card--back .brand__dot { background: var(--navy-soft); width: 30px; height: 30px; }
  .card--back .brand__name { font-size: 38px; }
  .person {
    position: absolute;
    left: 48px;
    top: 212px;
    color: var(--white);
  }
  .person__name {
    margin: 0;
    font-size: 24px;
    font-weight: 600;
    color: var(--gold);
    letter-spacing: 0.02em;
  }
  .person__title {
    margin: 4px 0 0;
    font-size: 19px;
    font-weight: 500;
    line-height: 1.3;
  }
  .contact {
    list-style: none;
    margin: 20px 0 0;
    padding: 0;
    font-size: 19px;
    font-weight: 500;
  }
  .contact__item {
    display: flex;
    align-items: flex-start;
    gap: 14px;
    margin-bottom: 6px;
    line-height: 1.3;
  }
  .contact__icon {
    width: 20px;
    height: 20px;
    flex: none;
    margin-top: 2px;
    fill: var(--gold);
  }
</style>
</head>
<body>
<main class="canvas">

  <section class="card card--front" aria-label="Card front">
    <svg class="card__shapes" viewBox="0 0 840 480" aria-hidden="true">
      <rect width="840" height="480" fill="var(--navy)"/>
      <circle cx="820" cy="10" r="480" fill="var(--gold)"/>
      <circle cx="820" cy="10" r="466" fill="var(--white)"/>
    </svg>

    <div class="brand">
      <span class="brand__dot"></span>
      <span class="brand__name">RV Spine &amp;<br>Vitality Center</span>
    </div>

    <div class="person">
      <h1 class="person__name">LUCINDA FERROW, M.D.</h1>
      <p class="person__title">Board Certified Hand and<br>Upper Extremity Surgeon</p>
      <ul class="contact">
        <li class="contact__item">
          <svg class="contact__icon" viewBox="0 0 24 24" aria-hidden="true"><path d="M6.6 10.8a15.1 15.1 0 0 0 6.6 6.6l2.2-2.2a1 1 0 0 1 1-.25 11.4 11.4 0 0 0 3.6.57 1 1 0 0 1 1 1V20a1 1 0 0 1-1 1A17 17 0 0 1 3 4a1 1 0 0 1 1-1h3.5a1 1 0 0 1 1 1c0 1.25.2 2.45.57 3.57a1 1 0 0 1-.25 1z"/></svg>
          <span>954-218-4630</span>
        </li>
        <li class="contact__item">
          <svg class="contact__icon" viewBox="0 0 24 24" aria-hidden="true"><path d="M7 2h10v5H7zM4 8h16a2 2 0 0 1 2 2v10a2 2 0 0 1-2 2H4a2 2 0 0 1-2-2V10a2 2 0 0 1 2-2zm3 4v2h2v-2zm4 0v2h2v-2zm4 0v2h2v-2zm-8 4v2h2v-2zm4 0v2h2v-2zm4 0v2h2v-2z"/></svg>
          <span>954-571-2846</span>
        </li>
        <li class="contact__item">
          <svg class="contact__icon" viewBox="0 0 24 24" aria-hidden="true"><path d="M2 5h20v14H2zm2 2v.4l8 5.3 8-5.3V7zm0 2.8V17h16V9.8l-8 5.3z"/></svg>
          <span>info@myrvspine.example</span>
        </li>
        <li class="contact__item">
          <svg class="contact__icon" viewBox="0 0 24 24" aria-hidden="true"><path d="M12 2a7 7 0 0 0-7 7c0 5 7 13 7 13s7-8 7-13a7 7 0 0 0-7-7zm0 9.5A2.5 2.5 0 1 1 12 6.5a2.5 2.5 0 0 1 0 5z"/></svg>
          <span>38915 North Bramble Ave<br>Willow Harbor, FL 34987</span>
        </li>
      </ul>
    </div>
  </section>

  <section class="card card--back" aria-label="Card back">
    <div class="brand">
      <span class="brand__dot"></span>
      <span class="brand__name">RV Spine &amp;<br>Vitality Center</span>
    </div>
  </section>

</main>
</body>
</html>
```